Physcial Activity & Parkinson's Disease Severity

We are very happy with the with the infographic below (on diet and PD progression). Now, we need a new infographic on the relationship between physical activity and PD progression.

Target Market(s)

Individuals with parkinonsonism (35-100 y), both genders, as well as their physicians, family members, support group leaders, etc.

Industry/Entity Type

Medicine

Requirements
Must have
• The same information as is listed in the top left corner of the previous infographic on Diet. (For more information: www.brightstepwellnessforall.com, For study info: www.TRVStudyQN.Holmecrest.edu), 2020, RT Vandorne, etc.
Nice to have
• It should fit in nicely with the other ones from a design standpoint.

```html
<!DOCTYPE html>
<html lang="en">
<head>
<meta charset="utf-8">
<title>Relationship Between Physical Activity &amp; PD Progression</title>
<link href="https://fonts.googleapis.com/css2?family=Merriweather:wght@700;900&family=Source+Sans+3:ital,wght@0,400;0,600;0,700;1,400;1,600;1,700&display=swap" rel="stylesheet">
<style>
  :root{
    --page:#f2f2f3;
    --panel:#e3e3e6;
    --navy:#2c3e98;
    --navy-line:#2f3a9a;
    --red:#c0152a;
    --poor:#b3121f;
    --fair:#e8714a;
    --good:#bcd46d;
    --excellent:#7bb83f;
    --ink:#1b1b1b;
    --grid:#cfcfd2;
    --strip:#d9d9dc;
    --g1:#0b5a28;
    --g2:#167a36;
    --g3:#2d6a2a;
    --g4:#3a7b2e;
    --g5:#508c38;
    --g6:#7fc15b;
    --g7:#a4d27a;
    --g8:#c4dd74;
  }
  *{box-sizing:border-box;margin:0;padding:0}
  html,body{width:1200px;height:1026px;overflow:hidden;background:var(--page)}
  body{position:relative;font-family:"Source Sans 3",sans-serif;color:var(--ink)}
  .serif{font-family:"Merriweather",serif}
  .block{position:absolute}
  .header-panel{left:28px;top:28px;width:468px;height:342px;background:var(--navy);color:#fff;overflow:hidden}
  .year-tab{position:absolute;right:0;top:0}
  .header-title{position:absolute;left:30px;top:52px;font-family:"Merriweather",serif;font-weight:900;font-size:31px;line-height:34px}
  .header-author{position:absolute;left:30px;top:164px;font-style:italic;font-size:17px}
  .header-dots{position:absolute;left:30px;top:196px;font-size:22px;font-weight:700;letter-spacing:1px}
  .header-info{position:absolute;left:30px;top:232px;font-size:16px;line-height:20px}
  .header-info em{display:block;font-style:italic}
  .header-info .url{display:block;font-family:"Merriweather",serif;font-weight:700;font-size:15px;margin-bottom:14px}
  .weight-panel{left:516px;top:28px;width:656px;height:342px;background:var(--panel)}
  .quality-band{left:28px;top:388px}
  .years-arrow{left:28px;top:542px;width:1144px;height:20px}
  .exercise-type{left:28px;top:596px}
  .exercise-freq{left:610px;top:596px}
  svg text{font-family:"Source Sans 3",sans-serif}
  .chart-title{font-family:"Merriweather",serif;font-weight:700;font-size:15px;fill:var(--ink)}
  .axis-label{font-style:italic;font-weight:600;font-size:14px;fill:var(--ink)}
  .tick{font-weight:700;font-size:13px;fill:var(--ink)}
  .val-red{font-style:italic;font-weight:700;font-size:13px;fill:var(--red)}
  .val-blue{font-style:italic;font-weight:700;font-size:13px;fill:var(--navy-line)}
  .pill{font-style:italic;font-weight:700;font-size:16px;fill:#fff}
  .bar-val{font-style:italic;font-weight:700;font-size:16px;fill:var(--ink)}
  .act{font-weight:700;font-size:13px;fill:var(--ink)}
  .pct{font-style:italic;font-weight:600;font-size:13px;fill:var(--ink)}
  .row-cap{font-size:12px;fill:var(--ink)}
  .ns{font-style:italic;font-size:9.5px;fill:#555}
</style>
</head>
<body>

<section class="block header-panel" aria-label="Study information">
  <svg class="year-tab" width="150" height="44" viewBox="0 0 150 44">
    <path d="M0 0 H150 V44 H46 C30 44 26 20 14 10 C8 4 4 0 0 0 Z" fill="var(--page)"/>
    <text x="92" y="34" text-anchor="middle" font-family="Merriweather, serif" font-weight="900" font-size="31" fill="var(--navy)">2020</text>
  </svg>
  <h1 class="header-title">Relationship Between<br>Physical Activity &amp;<br>PD Progression</h1>
  <p class="header-author">RT Vandorne et al.</p>
  <p class="header-dots">...</p>
  <div class="header-info">
    <em>For study details:</em>
    <span class="url">www.brightstepwellnessforall.com</span>
    <em>To participate in this study:</em>
    <span class="url">www.TRVStudyQN.Holmecrest.edu</span>
  </div>
</section>

<section class="block weight-panel" aria-label="Overweight individuals reported greater symptom severity">
  <svg width="656" height="342" viewBox="0 0 656 342">
    <text x="318" y="28" text-anchor="middle" class="chart-title">Overweight Indviduals Reported</text>
    <text x="318" y="48" text-anchor="middle" class="chart-title">Greator Symptom Severity</text>
    <g text-anchor="end" class="tick">
      <text x="106" y="286">0</text><text x="106" y="253">200</text><text x="106" y="220">400</text>
      <text x="106" y="187">600</text><text x="106" y="155">800</text><text x="106" y="122">1000</text>
      <text x="106" y="89">1200</text><text x="106" y="56">1400</text>
    </g>
    <text transform="translate(72 168) rotate(-90)" text-anchor="middle" class="axis-label">PRO-PD</text>
    <path d="M128 52 V282 H582" stroke="var(--ink)" stroke-width="2.5" fill="none"/>
    <g text-anchor="middle" class="tick">
      <text x="148" y="302">0</text><text x="190" y="302">1</text><text x="233" y="302">2</text><text x="275" y="302">3</text>
      <text x="318" y="302">4</text><text x="360" y="302">5</text><text x="402" y="302">6</text><text x="445" y="302">7</text>
      <text x="487" y="302">8</text><text x="530" y="302">9</text><text x="572" y="302">10</text>
    </g>
    <text x="360" y="324" text-anchor="middle" class="axis-label">Years Since Diagnosis</text>

    <polyline fill="none" stroke="var(--red)" stroke-width="2.5" points="148,162.6 190.4,150.1 232.8,157.3 275.2,161.2 317.6,143.8 360,146.5 402.4,116.2 444.8,143 487.2,114.3 529.6,100.1 572,85.8"/>
    <polyline fill="none" stroke="var(--navy-line)" stroke-width="2.5" points="148,186.4 190.4,188.5 232.8,183.7 275.2,169.5 317.6,180.5 360,155.3 402.4,143.2 444.8,134.3 487.2,143.2 529.6,134.5 572,117.5"/>
    <g fill="var(--red)">
      <circle cx="148" cy="162.6" r="3.5"/><circle cx="190.4" cy="150.1" r="3.5"/><circle cx="232.8" cy="157.3" r="3.5"/>
      <circle cx="275.2" cy="161.2" r="3.5"/><circle cx="317.6" cy="143.8" r="3.5"/><circle cx="360" cy="146.5" r="3.5"/>
      <circle cx="402.4" cy="116.2" r="3.5"/><circle cx="444.8" cy="143" r="3.5"/><circle cx="487.2" cy="114.3" r="3.5"/>
      <circle cx="529.6" cy="100.1" r="3.5"/><circle cx="572" cy="85.8" r="3.5"/>
    </g>
    <g fill="var(--navy-line)">
      <circle cx="148" cy="186.4" r="3.5"/><circle cx="190.4" cy="188.5" r="3.5"/><circle cx="232.8" cy="183.7" r="3.5"/>
      <circle cx="275.2" cy="169.5" r="3.5"/><circle cx="317.6" cy="180.5" r="3.5"/><circle cx="360" cy="155.3" r="3.5"/>
      <circle cx="402.4" cy="143.2" r="3.5"/><circle cx="444.8" cy="134.3" r="3.5"/><circle cx="487.2" cy="143.2" r="3.5"/>
      <circle cx="529.6" cy="134.5" r="3.5"/><circle cx="572" cy="117.5" r="3.5"/>
    </g>
    <g text-anchor="middle" class="val-red">
      <text x="142" y="152">727</text><text x="190" y="140">803</text><text x="233" y="147">759</text>
      <text x="275" y="151">735</text><text x="318" y="134">841</text><text x="360" y="136">825</text>
      <text x="402" y="106">1009</text><text x="445" y="160">846</text><text x="487" y="104">1021</text>
      <text x="530" y="90">1107</text><text x="572" y="76">1194</text>
    </g>
    <g text-anchor="middle" class="val-blue">
      <text x="144" y="204">582</text><text x="190" y="206">569</text><text x="233" y="201">598</text>
      <text x="275" y="187">685</text><text x="318" y="198">618</text><text x="360" y="173">771</text>
      <text x="402" y="161">845</text><text x="445" y="124">899</text><text x="487" y="161">845</text>
      <text x="530" y="152">898</text><text x="572" y="107">1001</text>
    </g>
    <rect x="168" y="78" width="118" height="26" rx="13" fill="var(--red)"/>
    <text x="227" y="97" text-anchor="middle" class="pill">Overweight</text>
    <rect x="397" y="178" width="124" height="24" rx="12" fill="var(--navy)"/>
    <text x="459" y="195" text-anchor="middle" class="pill" font-size="15">Not Overweight</text>
  </svg>
</section>

<section class="block quality-band" aria-label="Correlation between quality of life and PRO-PD score">
  <svg width="1144" height="154" viewBox="0 0 1144 154">
    <rect x="0" y="0" width="26" height="125" fill="#111"/>
    <text transform="translate(18 62) rotate(-90)" text-anchor="middle" class="axis-label" style="fill:#fff">PRO-PD Score</text>
    <g text-anchor="end" class="tick" font-size="12">
      <text x="60" y="9">2500</text><text x="60" y="33">2000</text><text x="60" y="58">1500</text>
      <text x="60" y="83">1000</text><text x="60" y="107">500</text><text x="60" y="132">0</text>
    </g>
    <rect x="64" y="0" width="1050" height="125" fill="var(--poor)"/>
    <polygon points="64,57 1114,12 1114,40" fill="#e9e6e6"/>
    <rect x="64" y="57" width="1050" height="18" fill="var(--fair)"/>
    <rect x="64" y="75" width="1050" height="25" fill="var(--good)"/>
    <rect x="64" y="100" width="1050" height="25" fill="var(--excellent)"/>
    <text font-family="Merriweather, serif" font-weight="700" font-size="15" fill="#fff">
      <tspan x="136" y="20">Correlation Between</tspan><tspan x="86" y="39">Quality of Life and PRO-PD Score</tspan>
    </text>
    <g text-anchor="end" font-size="14" font-style="italic" font-weight="600" fill="#fff">
      <text x="1106" y="70">Fair</text><text x="1106" y="93">Good</text><text x="1106" y="118">Excellent</text>
    </g>
    <rect x="1118" y="0" width="26" height="125" fill="#111"/>
    <text transform="translate(1136 62) rotate(-90)" text-anchor="middle" class="axis-label" style="fill:#fff">Quality Of Life</text>
    <polyline points="64,93.2 300,77.5 573,62 845,46.5" fill="none" stroke="#111" stroke-width="2.5"/>
    <g fill="#111">
      <circle cx="64" cy="93.2" r="5"/><circle cx="300" cy="77.5" r="5"/><circle cx="573" cy="62" r="5"/><circle cx="845" cy="46.5" r="5"/>
    </g>
    <g font-style="italic" font-weight="700" font-size="12" fill="#fff" text-anchor="middle">
      <text x="80" y="87">637</text><text x="300" y="70">950</text><text x="573" y="56">1260</text>
    </g>
    <text x="845" y="38" text-anchor="middle" font-style="italic" font-weight="700" font-size="12" fill="#111">1570</text>
    <g text-anchor="middle" class="tick" font-size="12">
      <text x="52" y="141">0</text><text x="160" y="141">5</text><text x="300" y="141">10</text><text x="436" y="141">15</text>
      <text x="573" y="141">20</text><text x="709" y="141">25</text><text x="845" y="141">30</text><text x="981" y="141">35</text>
    </g>
  </svg>
</section>

<div class="block years-arrow" aria-label="Years since diagnosis">
  <svg width="1144" height="20" viewBox="0 0 1144 20">
    <line x1="4" y1="10" x2="478" y2="10" stroke="#111" stroke-width="1.5"/>
    <line x1="660" y1="10" x2="1140" y2="10" stroke="#111" stroke-width="1.5"/>
    <path d="M0 10 L10 5 V15 Z M1144 10 L1134 5 V15 Z" fill="#111"/>
    <text x="569" y="15" text-anchor="middle" class="axis-label">Years Since Diagnosis</text>
  </svg>
</div>

<section class="block exercise-type" aria-label="Are some forms of exercise better than others">
  <svg width="560" height="400" viewBox="0 0 560 400">
    <text x="300" y="22" text-anchor="middle" class="chart-title">Are some Forms of Exercise Better Than Others?</text>
    <text transform="translate(18 170) rotate(-90)" text-anchor="middle" class="axis-label" font-size="13">Average Impact on PRO-PD Score</text>
    <g stroke="var(--grid)" stroke-width="1">
      <line x1="66" y1="40" x2="550" y2="40"/><line x1="66" y1="75" x2="550" y2="75"/><line x1="66" y1="110" x2="550" y2="110"/>
      <line x1="66" y1="145" x2="550" y2="145"/><line x1="66" y1="180" x2="550" y2="180"/><line x1="66" y1="215" x2="550" y2="215"/>
      <line x1="66" y1="285" x2="550" y2="285"/>
    </g>
    <line x1="66" y1="250" x2="550" y2="250" stroke="#999" stroke-width="1.5"/>
    <g text-anchor="end" class="tick" font-size="12">
      <text x="58" y="44">300</text><text x="58" y="79">250</text><text x="58" y="114">200</text><text x="58" y="149">150</text>
      <text x="58" y="184">100</text><text x="58" y="219">50</text><text x="58" y="254">0</text><text x="58" y="289">-50</text>
    </g>
    <g>
      <rect x="87" y="103.7" width="26" height="146.3" fill="var(--g1)"/>
      <rect x="135" y="172.3" width="26" height="77.7" fill="var(--g2)"/>
      <rect x="183" y="187.7" width="26" height="62.3" fill="var(--g3)"/>
      <rect x="231" y="191.9" width="26" height="58.1" fill="var(--g4)"/>
      <rect x="279" y="197.5" width="26" height="52.5" fill="var(--g5)"/>
      <rect x="327" y="217.8" width="26" height="32.2" fill="var(--g6)"/>
      <rect x="375" y="217.8" width="26" height="32.2" fill="var(--g6)"/>
      <rect x="423" y="226.9" width="26" height="23.1" fill="var(--g7)"/>
      <rect x="471" y="243" width="26" height="7" fill="var(--g7)"/>
      <rect x="519" y="248.6" width="26" height="1.4" fill="var(--g8)"/>
    </g>
    <g stroke="#111" stroke-width="1.5" fill="none">
      <path d="M100 75V124M95 75h10M95 124h10"/>
      <path d="M148 145V194M143 145h10M143 194h10"/>
      <path d="M196 162.5V208M191 162.5h10M191 208h10"/>
      <path d="M244 166V215M239 166h10M239 215h10"/>
      <path d="M292 176.5V218.5M287 176.5h10M287 218.5h10"/>
      <path d="M340 194V243M335 194h10M335 243h10"/>
      <path d="M388 187V246.5M383 187h10M383 246.5h10"/>
      <path d="M436 211.5V243M431 211.5h10M431 243h10"/>
      <path d="M484 215V267.5M479 215h10M479 267.5h10"/>
      <path d="M532 222V267.5M527 222h10M527 267.5h10"/>
    </g>
    <g class="act">
      <text transform="translate(104 70) rotate(-90)">Running</text>
      <text transform="translate(152 140) rotate(-90)">Other</text>
      <text transform="translate(200 157) rotate(-90)">Yoga</text>
      <text transform="translate(248 161) rotate(-90)">Hiking</text>
      <text transform="translate(296 171) rotate(-90)">Biking</text>
      <text transform="translate(344 189) rotate(-90)">Walking</text>
      <text transform="translate(392 182) rotate(-90)">Tai Chi</text>
      <text transform="translate(440 206) rotate(-90)">Dance</text>
      <text transform="translate(488 210) rotate(-90)">Steady Bout Boxing</text>
      <text transform="translate(536 217) rotate(-90)">Swimming</text>
    </g>
    <g text-anchor="end" class="bar-val">
      <text x="85" y="118">209</text><text x="132" y="186">111</text><text x="181" y="201">89</text>
      <text x="229" y="205">83</text><text x="277" y="211">75</text><text x="325" y="231">46</text>
      <text x="373" y="231">46</text><text x="421" y="240">33</text><text x="469" y="252">10</text><text x="517" y="257">2</text>
    </g>
    <g text-anchor="end" class="pct">
      <text transform="translate(110 304) rotate(-40)">9.9%</text>
      <text transform="translate(158 304) rotate(-40)">46.2%</text>
      <text transform="translate(206 304) rotate(-40)">22.5%</text>
      <text transform="translate(254 304) rotate(-40)">11.9%</text>
      <text transform="translate(302 304) rotate(-40)">25.0%</text>
      <text transform="translate(350 304) rotate(-40)">73.5%</text>
      <text transform="translate(398 304) rotate(-40)">10.0%</text>
      <text transform="translate(446 304) rotate(-40)">11.4%</text>
      <text transform="translate(494 304) rotate(-40)">6.8%</text>
      <text transform="translate(542 304) rotate(-40)">10.6%</text>
    </g>
    <rect x="0" y="366" width="560" height="22" fill="var(--strip)"/>
    <text x="280" y="382" text-anchor="middle" class="axis-label" font-size="12.5">Percentage of Participants Reporting Participation in Each Activity</text>
  </svg>
</section>

<section class="block exercise-freq" aria-label="Does the frequency of exercise matter">
  <svg width="562" height="400" viewBox="0 0 562 400">
    <text x="280" y="22" text-anchor="middle" class="chart-title">Does the Frequency of Exercise Matter?</text>
    <text transform="translate(30 200) rotate(-90)" text-anchor="middle" class="axis-label" font-size="13">% of Participants</text>
    <g stroke="var(--grid)" stroke-width="1">
      <line x1="130" y1="40" x2="130" y2="366"/><line x1="210" y1="40" x2="210" y2="366"/><line x1="250" y1="40" x2="250" y2="366"/>
      <line x1="290" y1="40" x2="290" y2="366"/><line x1="330" y1="40" x2="330" y2="366"/><line x1="370" y1="40" x2="370" y2="366"/>
      <line x1="410" y1="40" x2="410" y2="366"/><line x1="470" y1="40" x2="470" y2="366"/>
    </g>
    <line x1="170" y1="40" x2="170" y2="366" stroke="#aaa" stroke-width="1"/>

    <g class="row-cap">
      <text x="170" y="54">Exercise 30+ min/d, 7 days/wk</text>
      <text x="170" y="92">Exercise 30+ min/d, 6 days/wk</text>
      <text x="170" y="130">Exercise 30+ min/d, 5 days/wk</text>
      <text x="170" y="168">Exercise 30+ min/d, 4 days/wk</text>
      <text x="170" y="206">Exercise 30+ min/d, 3 days/wk</text>
      <text x="170" y="244">Exercise 30+ min/d, 2 days/wk</text>
      <text x="170" y="282">Exercise 30+ min/d, 1 days/wk</text>
      <text x="170" y="324">Exercise 30+ min/d, 0 days/wk</text>
    </g>
    <rect x="170" y="57" width="240.8" height="16" fill="var(--g1)"/>
    <rect x="170" y="95" width="233.6" height="16" fill="var(--g2)"/>
    <rect x="170" y="133" width="189.6" height="16" fill="var(--g3)"/>
    <rect x="170" y="171" width="183.2" height="16" fill="var(--g4)"/>
    <rect x="170" y="209" width="153.6" height="16" fill="var(--g6)"/>
    <rect x="170" y="247" width="16" height="16" fill="var(--g7)"/>
    <rect x="170" y="285" width="47.2" height="16" fill="var(--g8)"/>
    <g stroke="#111" stroke-width="1.5" fill="none">
      <path d="M370 65H442M370 60v10M442 60v10"/>
      <path d="M360 103H438M360 98v10M438 98v10"/>
      <path d="M330 141H392M330 136v10M392 136v10"/>
      <path d="M320 179H385M320 174v10M385 174v10"/>
      <path d="M295 217H370M295 212v10M370 212v10"/>
      <path d="M162 255H226M162 250v10M226 250v10"/>
      <path d="M154 293H232M154 288v10M232 288v10"/>
    </g>
    <g class="bar-val" font-size="15">
      <text x="448" y="70">-301</text><text x="444" y="108">-292</text><text x="398" y="146">-237</text>
      <text x="391" y="184">-229</text><text x="376" y="222">-192</text><text x="232" y="260">-20</text><text x="238" y="298">-59</text>
    </g>
    <g text-anchor="end" class="ns">
      <text x="552" y="258">Not Statistically Significant</text>
      <text x="552" y="296">Not Statistically Significant</text>
    </g>

    <g>
      <rect x="44" y="54" width="3" height="15" fill="var(--g1)"/>
      <rect x="44" y="92" width="3" height="15" fill="var(--g2)"/>
      <rect x="44" y="130" width="3" height="15" fill="var(--g3)"/>
      <rect x="44" y="168" width="3" height="15" fill="var(--g4)"/>
      <rect x="44" y="206" width="3" height="15" fill="var(--g6)"/>
      <rect x="44" y="244" width="3" height="15" fill="var(--g7)"/>
      <rect x="44" y="282" width="3" height="15" fill="var(--g8)"/>
      <rect x="44" y="316" width="3" height="15" fill="var(--red)"/>
    </g>
    <g class="tick" font-size="13" font-weight="600">
      <text x="56" y="66">20%</text><text x="56" y="104">15%</text><text x="56" y="142">17%</text><text x="56" y="180">15%</text>
      <text x="56" y="218">13%</text><text x="56" y="256">9%</text><text x="56" y="294">4%</text><text x="56" y="328">6%</text>
    </g>

    <rect x="0" y="366" width="562" height="22" fill="var(--strip)"/>
    <g text-anchor="middle" font-size="11" font-style="italic" fill="var(--ink)">
      <text x="130" y="381">50</text><text x="170" y="381">0</text><text x="210" y="381">-50</text><text x="250" y="381">-100</text>
      <text x="290" y="381">-150</text><text x="330" y="381">-200</text><text x="370" y="381">-250</text><text x="410" y="381">-300</text><text x="450" y="381">-400</text>
    </g>
    <text x="528" y="382" text-anchor="middle" class="axis-label" font-weight="700" font-size="14">PRO-PD</text>
  </svg>
</section>

</body>
</html>
```